Harmony Four Showcase
Date: Sunday Oct 2, 2022
When: 2-4 p.m.
Location: Brindle9 Alehouse
413 Marigold Wy #200, Sacramento, CA 95821
Tickets: www.Ticketwisp.example
General seating: $15 for adults and $10 for students

```html
<!DOCTYPE html>
<html lang="en">
<head>
<meta charset="utf-8">
<title>Harmony Four Showcase</title>
<link rel="stylesheet" href="https://fonts.googleapis.com/css2?family=Oswald:wght@400;500;600&family=Montserrat:wght@500;700&display=swap">
<style>
  :root {
    --page: #e9e7e4;
    --poster-deep: #1c0a09;
    --poster-mid: #44150f;
    --poster-warm: #7a2a12;
    --glow: #c2521c;
    --white: #ffffff;
    --orange: #ff9a1f;
    --orange-hot: #ff6f1a;
    --pink: #f0506a;
    --price-box: #ef6a5c;
  }
  * { margin: 0; padding: 0; box-sizing: border-box; }
  html, body { width: 1200px; height: 2400px; overflow: hidden; }
  body {
    background: var(--page);
    font-family: "Montserrat", Arial, sans-serif;
    position: relative;
  }
  .poster {
    position: absolute;
    left: 100px; top: 450px;
    width: 1000px; height: 1500px;
    overflow: hidden;
    background: linear-gradient(180deg, var(--poster-warm) 0%, var(--poster-mid) 45%, var(--poster-deep) 100%);
    color: var(--white);
  }
  .poster__photo {
    position: absolute;
    left: 0; top: 0;
    width: 1000px; height: 800px;
    background:
      radial-gradient(circle at 36% 20%, var(--glow) 0%, rgba(194,82,28,0.55) 22%, rgba(74,23,16,0) 55%),
      linear-gradient(180deg, rgba(0,0,0,0) 60%, var(--poster-mid) 100%);
  }
  .headline {
    position: absolute;
    right: 50px; top: 260px;
    text-align: right;
    font-family: "Oswald", "Arial Narrow", sans-serif;
    line-height: 0.95;
  }
  .headline__top { font-size: 160px; font-weight: 500; color: var(--white); }
  .headline__main {
    font-size: 196px; font-weight: 600;
    background: linear-gradient(180deg, var(--orange) 0%, var(--orange-hot) 100%);
    -webkit-background-clip: text; background-clip: text; color: transparent;
  }
  .headline__sub { font-size: 78px; font-weight: 500; color: var(--white); margin-top: 10px; letter-spacing: 1px; }
  .event-date {
    position: absolute; left: 50px; top: 800px;
    font-family: "Oswald", "Arial Narrow", sans-serif;
    font-weight: 500; font-size: 122px; color: var(--orange); line-height: 1;
  }
  .event-date sup { font-size: 64px; vertical-align: 48px; }
  .venue { position: absolute; left: 50px; top: 985px; }
  .venue__name {
    display: flex; align-items: center; gap: 14px;
    font-family: "Oswald", "Arial Narrow", sans-serif;
    font-weight: 500; font-size: 58px; color: var(--orange); line-height: 1;
  }
  .venue__pin { width: 36px; height: 48px; }
  .venue__address { font-size: 21px; font-weight: 500; margin-top: 14px; }
  .event-time {
    position: absolute; right: 50px; top: 960px;
    font-family: "Oswald", "Arial Narrow", sans-serif;
    font-weight: 500; font-size: 112px; line-height: 1;
  }
  .tickets { position: absolute; left: 50px; top: 1150px; }
  .tickets__label,
  .tickets__brand {
    font-family: "Oswald", "Arial Narrow", sans-serif;
    font-weight: 500; font-size: 56px; line-height: 1.1;
    color: var(--white);
  }
  .tickets__url { font-size: 32px; font-weight: 500; margin-top: 10px; }
  .pricing {
    position: absolute; right: 50px; top: 1135px;
    text-align: right;
    font-family: "Oswald", "Arial Narrow", sans-serif;
  }
  .pricing__note {
    font-family: "Montserrat", Arial, sans-serif;
    font-size: 21px; font-weight: 700; letter-spacing: 1px;
    line-height: 1; margin-bottom: 12px;
  }
  .pricing__row {
    font-size: 82px; font-weight: 500; color: var(--pink);
    line-height: 1.12;
  }
  .pricing__amount {
    display: inline-block;
    font-size: 62px; line-height: 1;
    background: var(--price-box); color: var(--white);
    padding: 4px 8px; margin-left: 8px;
    vertical-align: 6px;
  }
</style>
</head>
<body>
  <main class="poster">
    <div class="poster__photo" role="img" aria-label="Photo of a long-haired singer performing into a microphone under warm orange stage light"></div>

    <h1 class="headline">
      <div class="headline__top">HARMONY</div>
      <div class="headline__main">FOUR</div>
      <div class="headline__sub">SHOWCASE</div>
    </h1>

    <p class="event-date">2<sup>ND</sup> OCTOBER, 2022</p>

    <section class="venue">
      <div class="venue__name">
        <svg class="venue__pin" viewBox="0 0 24 32" aria-hidden="true">
          <path d="M12 0C5.4 0 0 5.3 0 11.9 0 20.8 12 32 12 32s12-11.2 12-20.1C24 5.3 18.6 0 12 0zm0 17a5 5 0 1 1 0-10 5 5 0 0 1 0 10z" fill="var(--orange)"/>
        </svg>
        BRINDLE9 ALEHOUSE
      </div>
      <p class="venue__address">413 Marigold Wy #200, Sacramento, CA 95821</p>
    </section>

    <p class="event-time">2-4 P.M</p>

    <section class="tickets">
      <p class="tickets__label">BOOK TICKETS AT</p>
      <p class="tickets__brand">TICKETWISP</p>
      <p class="tickets__url">www.Ticketwisp.example</p>
    </section>

    <section class="pricing">
      <p class="pricing__note">GENERAL SEATING</p>
      <p class="pricing__row">ADULTS<span class="pricing__amount">$15</span></p>
      <p class="pricing__row">STUDENTS<span class="pricing__amount">$10</span></p>
    </section>
  </main>
</body>
</html>
```